New Crowdfunding site Fundlark needs banner ads

I’m looking for 4 standard size banner ads for www.fundlark.example to be used by LinkaDeal Affiliates in order to bring new crowdfunding projects to the platform.
728x90
160x600
300x250
180x160

Succesful designers will put on our Mentors list so that the project owner can also get their specific project banners from our designers. Designers can also become our affiliates either to promote Fundlark.example or individual projects.
Updates

Please note updated brief

Thank you to those that have submitted designs so far.
Please be reminded that the invitation will close tomorrow after which we will make our choice

Thanks for input so far.
Please note project closes tomorrow (Sunday) after which we will choose.

Target Market(s)

Target is a project owner with a project requiring $10,000 or more in any field including business and/or non-profits. Any country.
Inventors, creatives, communities, hardware or software, consumer items,

Industry/Entity Type

Crowdfunding

Font styles to use
Sans Serif

Requirements
Must have
• Clear button call to action based on our USPs shown on the home page but especially the use of Affiliate Networks to promote their project to the widest possible audience.

Text and button text should be editable (see png preference).
Call to action could be based on "Free Crowdfunding Consultation - is your project viable" or "Get Your Free Guide to Succesful Crowdfunding"
Nice to have
• .png format preferred with separate objects.
Some animation preferred in the button.

```html
<!DOCTYPE html>
<html lang="en">
<head>
<meta charset="utf-8">
<title>Fundlark banner set</title>
<link rel="stylesheet" href="https://fonts.googleapis.com/css2?family=Lato:wght@300;400;700;900&display=swap">
<style>
  :root {
    --cream: #f1eedb;
    --blue: #3a53a4;
    --green: #22b24c;
    --purple: #c062a8;
    --lime: #d4dc2c;
    --white: #ffffff;
    --label: #111111;
    --caption: #666666;
  }
  * { box-sizing: border-box; margin: 0; padding: 0; }
  html, body { width: 1200px; height: 840px; overflow: hidden; background: var(--white); }
  body { position: relative; font-family: "Lato", sans-serif; color: var(--blue); }

  .banner { position: absolute; background: var(--cream); overflow: hidden; }
  .banner > * { position: absolute; }

  .headline { text-align: center; font-weight: 300; line-height: 1; white-space: nowrap; text-transform: uppercase; }
  .headline b { font-weight: 900; }

  .cta-tag { background: var(--green); color: var(--white); font-weight: 900; text-align: center; border-radius: 999px; white-space: nowrap; text-transform: uppercase; }
  .cta-box { background: var(--purple); color: var(--white); font-weight: 900; text-align: center; text-transform: uppercase; line-height: 1; white-space: nowrap; }
  .cta-box .free { color: var(--lime); }

  .hands { background: linear-gradient(90deg, #a5399a 0%, #e0237d 18%, #2eb04f 36%, #2aa4dc 54%, #f0872a 72%, #e02a6d 88%, #f2e52c 100%); }

  .brand { display: flex; align-items: center; font-weight: 700; color: var(--blue); white-space: nowrap; }
  .brand-dot { border-radius: 50%; background: var(--green); flex: none; }

  .size-label { position: absolute; font-family: "Lato", sans-serif; color: var(--label); font-weight: 400; line-height: 1; }

  .swatch { position: absolute; top: 702px; width: 90px; height: 85px; }
  .swatch-name { position: absolute; top: 789px; font-size: 12px; color: var(--caption); font-family: "Lato", sans-serif; }

  /* 160x600 skyscraper */
  .skyscraper { left: 24px; top: 18px; width: 204px; height: 759px; }
  .skyscraper .headline { left: 0; width: 204px; top: 55px; }
  .skyscraper .l-sm { font-size: 21px; display: block; margin-bottom: 1px; }
  .skyscraper .l-md { font-size: 28px; display: block; }
  .skyscraper .l-lg { font-size: 40px; display: block; font-weight: 900; }
  .skyscraper .cta-box { left: 12px; top: 229px; width: 179px; height: 173px; border-radius: 10px; padding-top: 14px; font-size: 20px; }
  .skyscraper .cta-box .free { font-size: 70px; display: block; margin-bottom: 4px; }
  .skyscraper .cta-tag { left: 34px; top: 218px; width: 142px; height: 17px; font-size: 13px; line-height: 17px; }
  .skyscraper .hands { left: 0; top: 417px; width: 204px; height: 252px; }
  .skyscraper .footer { left: 0; top: 669px; width: 204px; height: 90px; background: var(--white); }
  .skyscraper .brand { left: 8px; top: 688px; font-size: 23px; gap: 8px; }
  .skyscraper .brand-dot { width: 50px; height: 50px; }

  /* 728x90 leaderboard */
  .leaderboard { left: 257px; top: 12px; width: 921px; height: 113px; }
  .leaderboard .hands { left: 13px; top: 2px; width: 108px; height: 111px; }
  .leaderboard .headline { left: 136px; width: 500px; top: 8px; font-size: 25px; line-height: 1.02; }
  .leaderboard .cta-box { left: 136px; top: 64px; width: 495px; height: 38px; border-radius: 14px; font-size: 14px; line-height: 38px; padding-top: 4px; }
  .leaderboard .cta-tag { left: 310px; top: 56px; width: 146px; height: 19px; font-size: 14px; line-height: 19px; }
  .leaderboard .brand { left: 668px; top: 22px; font-size: 28px; gap: 10px; }
  .leaderboard .brand-dot { width: 70px; height: 70px; }

  /* 300x250 medium rectangle */
  .rectangle { left: 261px; top: 183px; width: 383px; height: 318px; }
  .rectangle .headline { left: 0; width: 383px; top: 30px; font-size: 19px; line-height: 1.02; }
  .rectangle .cta-box { left: 23px; top: 85px; width: 340px; height: 81px; border-radius: 10px; font-size: 18px; padding-top: 15px; }
  .rectangle .cta-box .free { font-size: 28px; display: block; margin-bottom: 1px; }
  .rectangle .cta-tag { left: 107px; top: 75px; width: 170px; height: 21px; font-size: 16px; line-height: 21px; }
  .rectangle .hands { left: 14px; top: 177px; width: 120px; height: 141px; }
  .rectangle .brand { left: 157px; top: 218px; font-size: 23px; gap: 8px; }
  .rectangle .brand-dot { width: 60px; height: 60px; }

  /* 180x160 small rectangle */
  .small { left: 332px; top: 577px; width: 228px; height: 201px; }
  .small .headline { left: 0; width: 228px; top: 18px; font-size: 10.5px; line-height: 1.05; }
  .small .cta-box { left: 14px; top: 51px; width: 204px; height: 48px; border-radius: 7px; font-size: 9.5px; padding-top: 9px; }
  .small .cta-box .free { font-size: 15px; display: block; }
  .small .cta-tag { left: 65px; top: 45px; width: 125px; height: 13px; font-size: 9px; line-height: 13px; }
  .small .hands { left: 8px; top: 104px; width: 82px; height: 97px; }
  .small .brand { left: 96px; top: 140px; font-size: 14px; gap: 5px; }
  .small .brand-dot { width: 34px; height: 34px; }
</style>
</head>
<body>

  <!-- 160x600 -->
  <section class="banner skyscraper">
    <h2 class="headline">
      <span class="l-sm">Many people in</span>
      <span class="l-sm">the world want</span>
      <span class="l-md">to <b>help you</b></span>
      <span class="l-sm" style="font-size:23px">to fulfill <b>your</b></span>
      <span class="l-lg">Dreams</span>
    </h2>
    <div class="cta-box"><span class="free">Free</span>Crowdfunding<br>Consultation<br>is your<br>project viable</div>
    <div class="cta-tag">Click here for</div>
    <div class="hands" role="img" aria-label="Illustration of many colourful raised hands"></div>
    <div class="footer"></div>
    <div class="brand"><span class="brand-dot"></span>Fundlark</div>
  </section>
  <div class="size-label" style="left:22px; top:791px; font-size:33px;">160x600</div>

  <!-- 728x90 -->
  <section class="banner leaderboard">
    <div class="hands" role="img" aria-label="Illustration of many colourful raised hands"></div>
    <h2 class="headline">Many people in the world want<br><b>to help you</b> to fulfill <b>your dreams</b></h2>
    <div class="cta-box"><span class="free">Free</span> Crowdfunding consultation - is your project viable</div>
    <div class="cta-tag">Click here for</div>
    <div class="brand"><span class="brand-dot"></span>Fundlark</div>
  </section>
  <div class="size-label" style="left:259px; top:129px; font-size:33px;">728x90</div>

  <!-- 300x250 -->
  <section class="banner rectangle">
    <h2 class="headline">Many people in the world want<br>to <b>help you</b> to fulfill <b>your dreams</b></h2>
    <div class="cta-box"><span class="free">Free</span>Crowdfunding consultation<br>is your project viable</div>
    <div class="cta-tag">Click here for</div>
    <div class="hands" role="img" aria-label="Illustration of many colourful raised hands"></div>
    <div class="brand"><span class="brand-dot"></span>Fundlark</div>
  </section>
  <div class="size-label" style="left:384px; top:512px; font-size:33px;">300x250</div>

  <!-- 180x160 -->
  <section class="banner small">
    <h2 class="headline">Many people in the world want<br>to <b>help you</b> to fulfill <b>your dreams</b></h2>
    <div class="cta-box"><span class="free">Free</span>Crowdfunding consultation<br>is your project viable</div>
    <div class="cta-tag">Click here for</div>
    <div class="hands" role="img" aria-label="Illustration of many colourful raised hands"></div>
    <div class="brand"><span class="brand-dot"></span>Fundlark</div>
  </section>
  <div class="size-label" style="left:387px; top:789px; font-size:31px;">180x160</div>

  <!-- Palette -->
  <div class="swatch" style="left:864px; background:var(--green);"></div>
  <div class="swatch" style="left:959px; background:var(--blue);"></div>
  <div class="swatch" style="left:1056px; background:var(--purple);"></div>
  <div class="swatch-name" style="left:862px;">green 00b200</div>
  <div class="swatch-name" style="left:960px;">blue 0000ff</div>
  <div class="swatch-name" style="left:1056px;">purple ff4dff</div>

</body>
</html>
```